Harbor Claim Advisors
Licensed Public Adjusters
Harbor Claim Advisors -
Creative Brief
Professional
Edwin Castellaro
Senior Adjuster
412 Birchwood Lane Marlow Bend, ST 00000
ejc@hcamail.example
We also need a business card for: Martin Glossenbury cell # 555-201-0148 email - mrg@hcamail.example all other info is the same

```html
<!DOCTYPE html>
<html lang="en">
<head>
<meta charset="utf-8">
<title>Harbor Claim Advisors – Stationery Set</title>
<link href="https://fonts.googleapis.com/css2?family=Montserrat:wght@400;600;700&display=swap" rel="stylesheet">
<style>
:root{
  --brand-blue:#1f45a3;
  --swoosh-grey:#c3c7cf;
  --paper:#ffffff;
  --stage:#f2f2f3;
  --ink:#2b2f3a;
  --rule:#8a8f99;
  --faint:#e3e6ee;
}
*{box-sizing:border-box;margin:0;padding:0}
html,body{width:1200px;height:662px;overflow:hidden;background:var(--stage);font-family:'Montserrat',sans-serif;color:var(--ink)}
.stage{position:relative;width:1200px;height:662px}
.sheet,.card,.envelope{position:absolute;background:var(--paper);box-shadow:0 1px 4px rgba(0,0,0,.18);overflow:hidden}
.header-swoosh{position:absolute;left:0;top:0;width:100%}
.wordmark{position:absolute;display:flex;align-items:center;gap:5px;font-weight:700;color:var(--brand-blue);white-space:nowrap}
.wordmark .dot{display:inline-block;border-radius:50%;background:var(--brand-blue)}
.wordmark.light{color:#fff}
.wordmark.light .dot{background:#fff}
.faint-mark{position:absolute;font-weight:700;color:var(--faint);white-space:nowrap;display:flex;align-items:center;gap:10px}
.faint-mark .dot{display:inline-block;border-radius:50%;background:var(--faint)}
/* sheets */
.fax-sheet{left:29px;top:120px;width:355px;height:516px}
.letter-sheet{left:413px;top:120px;width:355px;height:516px}
.sheet .wordmark{left:22px;top:64px;font-size:9px}
.sheet .wordmark .dot{width:9px;height:9px}
.fax-title{position:absolute;right:22px;top:102px;font-size:15px;font-weight:700;letter-spacing:1px}
.fax-table{position:absolute;left:22px;top:122px;width:311px;display:grid;grid-template-columns:40px 1fr 40px 1fr;border:1px solid var(--rule);font-size:6px}
.fax-table span{border-bottom:1px solid var(--rule);height:18px;line-height:18px;padding-left:4px}
.fax-table span.label,.fax-table span.field{border-right:1px solid var(--rule)}
.fax-table span:nth-last-child(-n+4){border-bottom:none}
.fax-options{position:absolute;left:22px;top:204px;width:311px;display:flex;justify-content:space-between;font-size:6px}
.fax-options li{list-style:none;display:flex;align-items:center;gap:3px}
.fax-options li::before{content:"";width:6px;height:6px;border:1px solid var(--rule)}
.sheet-footer{position:absolute;left:0;right:0;bottom:14px;text-align:center;font-size:4.5px;color:#555;letter-spacing:.2px;white-space:nowrap}
.sheet .faint-mark{left:40px;bottom:40px;font-size:44px}
.sheet .faint-mark .dot{width:36px;height:36px}
/* cards */
.card{width:139px;height:82px}
.card-a{left:845px;top:19px}
.card-b{left:994px;top:19px}
.card-c{left:845px;top:110px}
.card-d{left:994px;top:110px;background:var(--brand-blue)}
.card .wordmark{font-size:6px}
.card .wordmark .dot{width:6px;height:6px}
.card-a .wordmark,.card-b .wordmark{left:8px;top:30px}
.card-person{position:absolute;right:6px;top:5px;text-align:right;color:#fff}
.card-person strong{display:block;font-size:5px;font-weight:700}
.card-person em{display:block;font-style:normal;font-size:3.6px}
.card-contact{position:absolute;left:8px;bottom:7px;font-size:3.4px;line-height:1.45;color:#444;white-space:nowrap}
.card-c .wordmark,.card-d .wordmark{left:50%;top:50%;transform:translate(-50%,-50%);font-size:7px}
/* envelopes */
.envelope{width:389px}
.envelope-front{left:797px;top:216px;height:211px}
.envelope-front .wordmark{left:16px;top:58px;font-size:9px}
.envelope-front .wordmark .dot{width:9px;height:9px}
.return-address{position:absolute;left:16px;top:112px;font-size:4.5px;line-height:1.5;color:#444}
.envelope-front .faint-mark{left:120px;top:105px;font-size:40px}
.envelope-front .faint-mark .dot{width:32px;height:32px}
.envelope-back{left:797px;top:437px;height:187px}
.envelope-back .flap{position:absolute;left:0;top:0;width:100%}
.envelope-back .wordmark{left:50%;top:40px;transform:translateX(-50%);font-size:9px}
.envelope-back .wordmark .dot{width:9px;height:9px}
</style>
</head>
<body>
<main class="stage">

  <section class="sheet fax-sheet">
    <svg class="header-swoosh" viewBox="0 0 355 80" height="80" preserveAspectRatio="none" aria-hidden="true">
      <path d="M0 0H355V44C290 62 200 36 130 46 90 52 40 40 0 30Z" fill="var(--swoosh-grey)"/>
      <path d="M0 0H355V38C290 56 200 30 130 40 90 46 40 34 0 24Z" fill="#fff"/>
      <path d="M0 0H355V33C290 50 200 24 130 34 90 40 40 28 0 18Z" fill="var(--brand-blue)"/>
    </svg>
    <div class="wordmark"><i class="dot"></i>Harbor Claim Advisors</div>
    <h1 class="fax-title">FAX</h1>
    <div class="fax-table">
      <span class="label">To:</span><span class="field"></span><span class="label">From:</span><span></span>
      <span class="label">Fax:</span><span class="field"></span><span class="label">Pages:</span><span></span>
      <span class="label">Phone:</span><span class="field"></span><span class="label">Date:</span><span></span>
      <span class="label">Re:</span><span class="field"></span><span class="label">CC:</span><span></span>
    </div>
    <ul class="fax-options">
      <li>Urgent</li><li>For Review</li><li>Please Comment</li><li>Please Reply</li><li>Please Recycle</li>
    </ul>
    <div class="faint-mark" aria-hidden="true"><i class="dot"></i>HCA</div>
    <p class="sheet-footer">412 Birchwood Lane Marlow Bend, ST 00000 &nbsp;·&nbsp; 555-201-0148 &nbsp;·&nbsp; Fax 555-201-0172 &nbsp;·&nbsp; hcamail.example</p>
  </section>

  <section class="sheet letter-sheet">
    <svg class="header-swoosh" viewBox="0 0 355 80" height="80" preserveAspectRatio="none" aria-hidden="true">
      <path d="M0 0H355V44C290 62 200 36 130 46 90 52 40 40 0 30Z" fill="var(--swoosh-grey)"/>
      <path d="M0 0H355V38C290 56 200 30 130 40 90 46 40 34 0 24Z" fill="#fff"/>
      <path d="M0 0H355V33C290 50 200 24 130 34 90 40 40 28 0 18Z" fill="var(--brand-blue)"/>
    </svg>
    <div class="wordmark"><i class="dot"></i>Harbor Claim Advisors</div>
    <div class="faint-mark" aria-hidden="true"><i class="dot"></i>HCA</div>
    <p class="sheet-footer">412 Birchwood Lane Marlow Bend, ST 00000 &nbsp;·&nbsp; 555-201-0148 &nbsp;·&nbsp; Fax 555-201-0172 &nbsp;·&nbsp; hcamail.example</p>
  </section>

  <article class="card card-a">
    <svg class="header-swoosh" viewBox="0 0 139 30" height="30" preserveAspectRatio="none" aria-hidden="true">
      <path d="M0 0H139V24C110 30 70 18 0 22Z" fill="var(--swoosh-grey)"/>
      <path d="M0 0H139V21C110 27 70 15 0 18Z" fill="#fff"/>
      <path d="M0 0H139V18C110 24 70 12 0 14Z" fill="var(--brand-blue)"/>
    </svg>
    <div class="card-person"><strong>Edwin Castellaro</strong><em>Senior Adjuster</em></div>
    <div class="wordmark"><i class="dot"></i>Harbor Claim Advisors</div>
    <p class="card-contact">412 Birchwood Lane Marlow Bend, ST 00000<br>555-201-0148 · ejc@hcamail.example</p>
  </article>

  <article class="card card-b">
    <svg class="header-swoosh" viewBox="0 0 139 30" height="30" preserveAspectRatio="none" aria-hidden="true">
      <path d="M0 0H139V24C110 30 70 18 0 22Z" fill="var(--swoosh-grey)"/>
      <path d="M0 0H139V21C110 27 70 15 0 18Z" fill="#fff"/>
      <path d="M0 0H139V18C110 24 70 12 0 14Z" fill="var(--brand-blue)"/>
    </svg>
    <div class="card-person"><strong>Martin Glossenbury</strong><em>Field Adjuster</em></div>
    <div class="wordmark"><i class="dot"></i>Harbor Claim Advisors</div>
    <p class="card-contact">412 Birchwood Lane Marlow Bend, ST 00000<br>555-201-0148 · mrg@hcamail.example</p>
  </article>

  <article class="card card-c">
    <div class="wordmark"><i class="dot"></i>Harbor Claim Advisors</div>
  </article>

  <article class="card card-d">
    <div class="wordmark light"><i class="dot"></i>Harbor Claim Advisors</div>
  </article>

  <section class="envelope envelope-front">
    <svg class="header-swoosh" viewBox="0 0 389 60" height="60" preserveAspectRatio="none" aria-hidden="true">
      <path d="M0 0H389V40C300 56 200 30 120 38 70 43 30 34 0 30Z" fill="var(--swoosh-grey)"/>
      <path d="M0 0H389V35C300 50 200 25 120 33 70 38 30 28 0 24Z" fill="#fff"/>
      <path d="M0 0H389V30C300 45 200 20 120 28 70 33 30 22 0 18Z" fill="var(--brand-blue)"/>
    </svg>
    <div class="wordmark"><i class="dot"></i>Harbor Claim Advisors</div>
    <p class="return-address">412 Birchwood Lane<br>Marlow Bend, ST 00000</p>
    <div class="faint-mark" aria-hidden="true"><i class="dot"></i>HCA</div>
  </section>

  <section class="envelope envelope-back">
    <svg class="flap" viewBox="0 0 389 90" height="90" preserveAspectRatio="none" aria-hidden="true">
      <path d="M0 0H389V62L194 90 0 62Z" fill="var(--swoosh-grey)"/>
      <path d="M0 0H389V56L194 84 0 56Z" fill="var(--brand-blue)"/>
    </svg>
    <div class="wordmark light"><i class="dot"></i>Harbor Claim Advisors</div>
  </section>

</main>
</body>
</html>
```